Plakate für Charity Unternehmen
Zielgruppe
Orek ist ein weltweit agierendes Charity Unternehmen.
Aufgabenstellung
Wir benötigen ein 'Plakat' Design, mit dem Zweck dieses Design als Banner, Sticker oder als Schild an unseren Projekten anzubringen. Das Schild soll in zwei verschiedenen Layouts geliefert werden.
1. Eine Art Blanko Version in der das Logo und das Motto eingearbeitet sind. Dieser Teil nimmt rund 1/3 des Plakats ein. Der Rest hat einen Freiraum auf dem wir Namen der Spender oder kooperative Charity Logos einsetzen können. Diese Version wird für Zusammenarbeit verwendet.
2. Eine zweite Version nimmt das gesamte Plakat ein, hier findet sich das Logo und das Motto welche das ganze Plakat einnehmen.
In beiden Fällen sollte die Aufteilung sauber und gut leserlich sein. Das Plakat wird in Auflösungen von bis zu 1,5m mal 1m gedruckt, sollte dementsprechend also die richtige Auflösung haben. Außerdem sollten Photoshop Datei möglichst mitgeliefert werden damit wir wenn nötig Namen und Logos einsetzen können.
Das einzuarbeitende Motto lautet:
إنما المؤمنون أخوة
Das Plakat sollte im Querformat sein und die Hintergrundfarbe sollte schwarz oder weiß sein.
Anbei befindet sich eine Beispieldatei wie das Plakat an den Projekten angebracht wird.

```html
<!DOCTYPE html>
<html lang="de">
<head>
<meta charset="utf-8">
<title>Orek Schild – zwei Layouts</title>
<link rel="stylesheet" href="https://fonts.googleapis.com/css2?family=Cairo:wght@600;700&display=swap">
<style>
  :root {
    --canvas-bg: #eeeeee;
    --poster-bg: #ffffff;
    --gold-light: #d9b466;
    --gold-dark: #b8903e;
    --accent-red: #d4392a;
    --accent-red-dark: #b02a1f;
    --accent-blue: #3a8fd6;
    --accent-blue-dark: #1f6db4;
    --brand-navy: #27306b;
    --text-light: #ffffff;
  }
  html, body {
    margin: 0;
    padding: 0;
    width: 1001px;
    height: 1200px;
    overflow: hidden;
    background: var(--canvas-bg);
  }
  .canvas {
    position: relative;
    width: 1001px;
    height: 1200px;
  }
  .poster {
    position: absolute;
    left: 108px;
    width: 785px;
    height: 528px;
    background: var(--poster-bg);
    overflow: hidden;
  }
  .poster--partner { top: 60px; }
  .poster--full { top: 612px; }
  .poster__shapes {
    position: absolute;
    inset: 0;
    width: 100%;
    height: 100%;
  }
  .brand {
    position: absolute;
    left: 0;
    width: 100%;
    display: flex;
    flex-direction: column;
    align-items: center;
  }
  .brand__mark {
    border-radius: 50%;
    background: linear-gradient(180deg, var(--gold-light), var(--gold-dark));
  }
  .brand__name {
    font-family: "Cairo", sans-serif;
    font-weight: 700;
    color: var(--brand-navy);
    letter-spacing: 4px;
    line-height: 1;
  }
  .poster--partner .brand { top: 58px; }
  .poster--partner .brand__mark { width: 130px; height: 130px; margin-bottom: 22px; }
  .poster--partner .brand__name { font-size: 52px; margin-left: -20px; }
  .poster--full .brand { top: 26px; }
  .poster--full .brand__mark { width: 120px; height: 120px; margin-bottom: 14px; }
  .poster--full .brand__name { font-size: 46px; }
  .motto {
    position: absolute;
    display: flex;
    align-items: center;
    justify-content: center;
    background: linear-gradient(180deg, var(--gold-light), var(--gold-dark));
    color: var(--text-light);
    font-family: "Cairo", sans-serif;
    font-weight: 700;
    font-size: 72px;
    line-height: 1;
    direction: rtl;
  }
  .poster--partner .motto { left: 0; top: 331px; width: 708px; height: 120px; }
  .poster--full .motto { left: 60px; top: 228px; width: 725px; height: 120px; }
</style>
</head>
<body>
<main class="canvas">

  <section class="poster poster--partner" aria-label="Schild für Zusammenarbeit">
    <svg class="poster__shapes" viewBox="0 0 785 528" aria-hidden="true">
      <polygon points="550,0 785,0 785,216" fill="var(--accent-red)"/>
      <polygon points="640,0 785,0 785,140" fill="var(--accent-red-dark)"/>
      <polygon points="0,295 0,528 216,528" fill="var(--accent-blue)"/>
      <polygon points="0,390 0,528 120,528" fill="var(--accent-blue-dark)"/>
    </svg>
    <div class="brand">
      <div class="brand__mark"></div>
      <div class="brand__name">SOLARA</div>
    </div>
    <div class="motto">إنما المؤمنون أخوة</div>
  </section>

  <section class="poster poster--full" aria-label="Schild Vollversion">
    <svg class="poster__shapes" viewBox="0 0 785 528" aria-hidden="true">
      <polygon points="0,0 252,0 0,240" fill="var(--accent-blue)"/>
      <polygon points="0,0 140,0 0,130" fill="var(--accent-blue-dark)"/>
      <polygon points="530,0 785,0 785,240" fill="var(--accent-red)"/>
      <polygon points="640,0 785,0 785,150" fill="var(--accent-red-dark)"/>
    </svg>
    <div class="brand">
      <div class="brand__mark"></div>
      <div class="brand__name">SOLARA</div>
    </div>
    <div class="motto">إنما المؤمنون أخوة</div>
  </section>

</main>
</body>
</html>
```